Marlow Sky Charter E-mail Signature

Need to create an email signature for Marlow Sky Charter. Signature should include the Marlow logo and the associated QFTR member logo

```html
<!DOCTYPE html>
<html lang="en">
<head>
<meta charset="utf-8">
<title>Marlow Sky Charter – E-mail Signatures</title>
<link rel="stylesheet" href="https://fonts.googleapis.com/css2?family=Montserrat:wght@400;500;600;700&display=swap">
<style>
  :root {
    --page: #e4e5e7;
    --card: #ffffff;
    --brand-blue: #1761b0;
    --ink: #111111;
    --ink-soft: #333333;
    --rule: #c9c9c9;
    --rule-grey: #bdbdbd;
  }
  * { box-sizing: border-box; margin: 0; padding: 0; }
  html, body {
    width: 1083px; height: 1200px; overflow: hidden;
    background: var(--page);
    font-family: "Montserrat", sans-serif;
    color: var(--ink);
  }
  .signature {
    position: absolute; left: 94px; width: 885px;
    background: var(--card);
  }
  .signature--classic { top: 88px; height: 281px; }
  .signature--stacked { top: 472px; height: 248px; }
  .signature--divided { top: 819px; height: 280px; }
  .signature__band {
    position: absolute; left: 0; bottom: 0; width: 100%; height: 16px;
    background: var(--brand-blue);
  }
  .abs { position: absolute; }

  .brand-mark { display: flex; align-items: center; gap: 9px; width: 180px; }
  .brand-mark__dot { flex: none; width: 14px; height: 14px; border-radius: 50%; background: var(--brand-blue); }
  .brand-mark__name {
    display: flex; flex-direction: column;
    font-weight: 700; font-size: 17px; line-height: 19px; letter-spacing: .6px;
    color: var(--brand-blue); white-space: nowrap;
  }

  .divider { position: absolute; width: 2px; background: var(--brand-blue); }
  .divider--thin { width: 1px; background: var(--rule-grey); }

  .person__name { font-size: 25px; font-weight: 700; line-height: 1; white-space: nowrap; }
  .person__name--blue { color: var(--brand-blue); font-weight: 600; }
  .person__role { font-size: 15.5px; color: var(--ink-soft); white-space: nowrap; }
  .person__role--caps { font-size: 11.5px; font-weight: 700; color: var(--ink); letter-spacing: .3px; text-transform: uppercase; }

  .contact { font-size: 13px; line-height: 16.5px; color: var(--ink-soft); white-space: nowrap; }
  .contact__label { font-weight: 700; color: var(--ink); }
  .contact__rule { height: 1px; width: 204px; background: var(--rule); margin: 8px 0 9px; }

  .member { display: flex; align-items: center; gap: 8px; }
  .member__shape { flex: none; width: 30px; height: 20px; border-radius: 50%; background: var(--brand-blue); }
  .member__text { position: relative; line-height: 1; }
  .member__label { position: absolute; right: 2px; top: -9px; font-size: 7px; color: var(--ink); white-space: nowrap; }
  .member__name { font-size: 22px; font-weight: 500; letter-spacing: 2px; color: var(--ink); }
  .member--small .member__shape { width: 26px; height: 17px; }
  .member--small .member__name { font-size: 19px; }

  .social { display: flex; gap: 8px; }
  .social__dot { width: 26px; height: 26px; border-radius: 50%; background: var(--brand-blue); }
</style>
</head>
<body>

<section class="signature signature--classic">
  <div class="abs brand-mark" style="left:56px; top:113px;">
    <span class="brand-mark__dot"></span>
    <span class="brand-mark__name"><span>MARLOW</span><span>SKY CHARTER</span></span>
  </div>
  <div class="divider" style="left:264px; top:75px; height:112px;"></div>
  <h1 class="abs person__name" style="left:307px; top:50px;">Adrian Kessler</h1>
  <p class="abs person__role" style="left:307px; top:82px;">Marketing Expert</p>
  <div class="abs contact" style="left:307px; top:116px;">
    <div class="contact__label">address</div>
    <div>Your Street Address Her</div>
    <div>New Your Sity Aip - 000</div>
    <div class="contact__rule"></div>
    <div>p : 00 123 456 7890</div>
    <div>e : username@marlowsky.com</div>
    <div>w : www.marlowskycharter.com</div>
  </div>
  <div class="divider" style="left:618px; top:75px; height:112px;"></div>
  <div class="abs member" style="left:663px; top:101px;">
    <span class="member__shape"></span>
    <span class="member__text">
      <span class="member__label">member of</span>
      <span class="member__name">QFTR</span>
    </span>
  </div>
  <div class="abs social" style="left:666px; top:163px;" role="img" aria-label="Social profile links">
    <span class="social__dot"></span><span class="social__dot"></span><span class="social__dot"></span><span class="social__dot"></span>
  </div>
  <div class="signature__band"></div>
</section>

<section class="signature signature--stacked">
  <div class="abs brand-mark" style="left:56px; top:99px;">
    <span class="brand-mark__dot"></span>
    <span class="brand-mark__name"><span>MARLOW</span><span>SKY CHARTER</span></span>
  </div>
  <h2 class="abs person__name person__name--blue" style="left:322px; top:42px;">Adrian Kessler</h2>
  <p class="abs person__role person__role--caps" style="left:322px; top:79px;">Marketing Expert</p>
  <div class="abs social" style="left:320px; top:165px;" role="img" aria-label="Social profile links">
    <span class="social__dot"></span><span class="social__dot"></span><span class="social__dot"></span><span class="social__dot"></span>
  </div>
  <div class="abs contact" style="left:642px; top:36px;">
    <div class="contact__label">address</div>
    <div>Your Street Address Her</div>
    <div>New Your Sity Aip - 000</div>
    <div class="contact__rule"></div>
    <div>p : 00 123 456 7890</div>
    <div>e : username@marlowsky.com</div>
    <div>w : www.marlowskycharter.com</div>
  </div>
  <div class="abs member member--small" style="left:642px; top:182px;">
    <span class="member__shape"></span>
    <span class="member__text">
      <span class="member__label">member of</span>
      <span class="member__name">QFTR</span>
    </span>
  </div>
  <div class="signature__band"></div>
</section>

<section class="signature signature--divided">
  <div class="abs brand-mark" style="left:56px; top:113px;">
    <span class="brand-mark__dot"></span>
    <span class="brand-mark__name"><span>MARLOW</span><span>SKY CHARTER</span></span>
  </div>
  <div class="divider divider--thin" style="left:275px; top:30px; height:209px;"></div>
  <h2 class="abs person__name person__name--blue" style="left:322px; top:58px;">Adrian Kessler</h2>
  <p class="abs person__role person__role--caps" style="left:322px; top:92px;">Marketing Expert</p>
  <div class="abs social" style="left:320px; top:181px;" role="img" aria-label="Social profile links">
    <span class="social__dot"></span><span class="social__dot"></span><span class="social__dot"></span><span class="social__dot"></span>
  </div>
  <div class="divider divider--thin" style="left:602px; top:30px; height:209px;"></div>
  <div class="abs contact" style="left:642px; top:51px;">
    <div class="contact__label">address</div>
    <div>Your Street Address Her</div>
    <div>New Your Sity Aip - 000</div>
    <div class="contact__rule"></div>
    <div>p : 00 123 456 7890</div>
    <div>e : username@marlowsky.com</div>
    <div>w : www.marlowskycharter.com</div>
  </div>
  <div class="abs member member--small" style="left:642px; top:198px;">
    <span class="member__shape"></span>
    <span class="member__text">
      <span class="member__label">member of</span>
      <span class="member__name">QFTR</span>
    </span>
  </div>
  <div class="signature__band"></div>
</section>

</body>
</html>
```